********Quiet Lantern Hawaii Needs A Business Card Design********

We need a logo design for a company based in Hawaii called "Quiet Lantern". We are an audio video "AV" and automation company that does home theaters, lighting and shade control, sound systems, security system, surveillance systems, central vacuum systems, and more. Our company mission is to "Simplify Technology" for our clients. Everything we do aims to make thing simple and reliable for our customers.
The feel of our company is fun, but luxurious. Our colors are red, black, and silver or gray.
The final design of the logo should communicate simplicity, fun, edgy and luxury.
I have included both color versions of our company logo and the shirts that we are looking at making to give you a feel of what we're going for.
I would like our company mission statement to be somewhere on the card and I would like the card to be two sided or I'm open to creative looking cards as well.

I need the following to be on the card somewhere

"Quiet Lantern Hawaii makes living with technology simple and enjoyable by providing reliable, user-friendly systems and the best customer service possible."

Office / Fax: (808) 555-3162
Direct: (808) 555-3162 ext.101
marty@quietlanternhi.example
quietlanternhi.example
Marcus Beddoe

Automation Systems
Lighting & Shade Control
Home Theater Installation & Design
Distributed Audio Video
High Definition Camera Systems
Burglar & Fire Alarms
Central Vacuum

Thank you for your time

Target Market(s)

High End Luxury Market

Industry/Entity Type

Security

Requirements
Must have
• "Quiet Lantern Hawaii makes living with technology simple and enjoyable by providing reliable, user-friendly systems and the best customer service possible."

marty@quietlanternhi.example
quietlanternhi.example
Marcus Beddoe

Automation Systems
Lighting & Shade Control
Distributed Audio Video
Burglar & Fire Alarms
Central Vacuum

```html
<!DOCTYPE html>
<html lang="en">
<head>
<meta charset="utf-8">
<title>Quiet Lantern Hawaii – Business Card</title>
<link rel="stylesheet" href="https://fonts.googleapis.com/css2?family=Exo+2:wght@400;500;600;700&display=swap">
<style>
  :root {
    --stage: #e6e2dc;
    --card-white: #ffffff;
    --card-dark: #333333;
    --brand-red: #c8202f;
    --ink: #3a3a3a;
    --ink-soft: #666666;
    --text-light: #ffffff;
    --text-soft: #e2e2e2;
  }
  * { box-sizing: border-box; margin: 0; padding: 0; }
  html, body {
    width: 1200px; height: 870px; overflow: hidden;
    background: var(--stage);
    font-family: "Exo 2", sans-serif;
  }
  .stage {
    position: relative; width: 1200px; height: 870px;
    display: flex; flex-direction: column; align-items: center; justify-content: center; gap: 60px;
  }
  .card {
    position: relative; width: 600px; height: 343px;
    box-shadow: 0 10px 28px rgba(0,0,0,0.22);
    overflow: hidden;
  }
  .card-back { background: var(--card-white); }
  .card-front { background: var(--card-dark); }
  .front-shape { position: absolute; inset: 0; width: 600px; height: 343px; }

  .brand {
    position: absolute; left: 38px; top: 130px;
    display: flex; align-items: center; gap: 12px;
  }
  .brand-dot {
    width: 30px; height: 30px; border-radius: 50%;
    background: var(--brand-red); flex: none;
  }
  .brand-name {
    color: var(--ink); font-weight: 700; font-size: 21px; line-height: 1.1;
    letter-spacing: 0.5px; text-transform: uppercase;
  }
  .brand-name span { display: block; font-size: 13px; letter-spacing: 6px; }

  .contact {
    position: absolute; right: 32px; top: 32px;
    text-align: right; color: var(--text-light);
  }
  .person-name { font-size: 20px; font-weight: 600; letter-spacing: 1.5px; text-transform: uppercase; }
  .person-role { font-size: 13px; color: var(--text-soft); margin-top: 2px; }
  .address { margin-top: 32px; font-size: 12.5px; line-height: 1.45; color: var(--text-soft); }
  .lines { margin-top: 22px; list-style: none; font-size: 12.5px; color: var(--text-soft); }
  .lines li { display: flex; justify-content: flex-end; align-items: center; gap: 8px; height: 21px; white-space: nowrap; }
  .lines svg { width: 11px; height: 11px; flex: none; fill: none; stroke: var(--text-light); stroke-width: 1.6; }

  .back-band { position: absolute; left: 0; top: 0; bottom: 0; width: 14px; background: var(--card-dark); }
  .back-band::after { content: ""; position: absolute; right: -6px; top: 0; bottom: 0; width: 6px; background: var(--brand-red); }
  .back-content { position: absolute; left: 52px; right: 40px; top: 36px; color: var(--ink); }
  .mission-label {
    font-size: 12px; font-weight: 600; letter-spacing: 3px; text-transform: uppercase; color: var(--brand-red);
  }
  .mission { margin-top: 8px; font-size: 14px; line-height: 1.5; font-weight: 500; }
  .rule { margin: 18px 0 16px; height: 2px; width: 60px; background: var(--brand-red); border: 0; }
  .services {
    list-style: none; display: grid; grid-template-columns: 1fr 1fr; column-gap: 20px; row-gap: 7px;
    font-size: 12.5px; color: var(--ink-soft);
  }
  .services li { display: flex; align-items: center; gap: 8px; }
  .services li::before { content: ""; width: 6px; height: 6px; background: var(--brand-red); flex: none; }
  .back-web {
    position: absolute; right: 40px; bottom: 26px;
    font-size: 12.5px; font-weight: 600; letter-spacing: 1px; color: var(--ink);
  }
</style>
</head>
<body>
<main class="stage">
  <section class="card card-front" aria-label="Business card front">
    <svg class="front-shape" viewBox="0 0 600 343" aria-hidden="true">
      <path d="M0 0 H232 Q330 171 232 343 H0 Z" fill="var(--brand-red)"/>
      <path d="M0 0 H218 Q316 171 218 343 H0 Z" fill="var(--card-dark)"/>
      <path d="M0 0 H210 Q306 171 210 343 H0 Z" fill="var(--card-white)"/>
    </svg>
    <div class="brand">
      <div class="brand-dot"></div>
      <div class="brand-name">Quiet Lantern<span>Hawaii</span></div>
    </div>
    <div class="contact">
      <p class="person-name">Marcus Beddoe</p>
      <p class="person-role">Managing Director</p>
      <p class="address">27 Palm Crest Lane, Suite 4<br>Kahului</p>
      <ul class="lines">
        <li>Office / Fax: (808) 555-3162
          <svg viewBox="0 0 12 12"><path d="M2 1 L4.5 1 L5 4 L3.6 5 Q5 7.6 7 8.4 L8 7 L11 7.5 L11 10 Q6 11 2 6 Q1 3.5 2 1 Z"/></svg></li>
        <li>Direct: (808) 555-3162 ext.101
          <svg viewBox="0 0 12 12"><rect x="3" y="1" width="6" height="10" rx="1"/></svg></li>
        <li>marty@quietlanternhi.example
          <svg viewBox="0 0 12 12"><rect x="1" y="2.5" width="10" height="7"/><path d="M1 2.5 L6 6.5 L11 2.5"/></svg></li>
        <li>quietlanternhi.example
          <svg viewBox="0 0 12 12"><circle cx="6" cy="6" r="5"/><path d="M1 6 H11 M6 1 Q3 6 6 11 Q9 6 6 1"/></svg></li>
      </ul>
    </div>
  </section>

  <section class="card card-back" aria-label="Business card back">
    <div class="back-band"></div>
    <div class="back-content">
      <p class="mission-label">Simplify Technology</p>
      <p class="mission">Quiet Lantern Hawaii makes living with technology simple and enjoyable by providing reliable, user-friendly systems and the best customer service possible.</p>
      <hr class="rule">
      <ul class="services">
        <li>Automation Systems</li>
        <li>Lighting &amp; Shade Control</li>
        <li>Home Theater Installation &amp; Design</li>
        <li>Distributed Audio Video</li>
        <li>High Definition Camera Systems</li>
        <li>Burglar &amp; Fire Alarms</li>
        <li>Central Vacuum</li>
      </ul>
    </div>
    <p class="back-web">quietlanternhi.example</p>
  </section>
</main>
</body>
</html>
```